2 graphics needed for brochure

I have 2 graphs needed for a brochure that our group is producing. They need to convey a high tech and innovation approach.

Industry/Entity Type

Graphic Design

```html
<!DOCTYPE html>
<html lang="en">
<head>
<meta charset="utf-8">
<title>Management/Resolution by academic and industry collaborators</title>
<link rel="stylesheet" href="https://fonts.googleapis.com/css2?family=Roboto+Condensed:wght@300&family=Roboto:wght@400;900&display=swap">
<style>
  :root {
    --bg: #ffffff;
    --band: #dcdcdc;
    --fold: #5b1d3c;
    --title: #4a4a4a;
    --text: #1e1e1e;
    --num: #ffffff;
    --blue-a: #22b6f0; --blue-b: #0a7fc2;
    --yellow-a: #ffd400; --yellow-b: #e8900f;
    --green-a: #36bb57; --green-b: #10733a;
    --pink-a: #ea2d7f; --pink-b: #a40f4c;
    --teal-a: #33b2c9; --teal-b: #117b92;
    --purple-a: #a866c6; --purple-b: #662c86;
  }
  * { margin: 0; padding: 0; box-sizing: border-box; }
  html, body { width: 720px; height: 1200px; overflow: hidden; background: var(--bg); }
  .canvas { position: relative; width: 720px; height: 1200px; }
  .title {
    position: absolute; top: 50px; left: 0; width: 720px; text-align: center;
    font-family: "Roboto Condensed", "Arial Narrow", sans-serif; font-weight: 300;
    font-size: 31px; line-height: 38px; color: var(--title);
  }
  .step { position: absolute; left: 0; width: 720px; height: 138px; }
  .step svg { position: absolute; left: 0; top: 0; }
  .step-number {
    position: absolute; left: 108px; top: 14px; width: 84px; text-align: center;
    font-family: "Roboto", Arial, sans-serif; font-weight: 900; font-size: 42px;
    line-height: 48px; color: var(--num); letter-spacing: 1px;
    text-shadow: 0 2px 3px rgba(0,0,0,0.25);
  }
  .step-text {
    position: absolute; left: 214px; width: 420px; top: 30px;
    font-family: "Roboto", Arial, sans-serif; font-weight: 400;
    font-size: 15.5px; line-height: 25px; color: var(--text);
  }
  .step-text.inset { left: 226px; }
</style>
</head>
<body>
<div class="canvas">
  <h1 class="title">Management/Resolution by<br>academic and industry collaborators</h1>

  <svg width="0" height="0" style="position:absolute">
    <defs>
      <linearGradient id="g-blue" x1="0" y1="0" x2="0" y2="1"><stop offset="0" stop-color="var(--blue-a)"/><stop offset="1" stop-color="var(--blue-b)"/></linearGradient>
      <linearGradient id="g-yellow" x1="0" y1="0" x2="0" y2="1"><stop offset="0" stop-color="var(--yellow-a)"/><stop offset="1" stop-color="var(--yellow-b)"/></linearGradient>
      <linearGradient id="g-green" x1="0" y1="0" x2="0" y2="1"><stop offset="0" stop-color="var(--green-a)"/><stop offset="1" stop-color="var(--green-b)"/></linearGradient>
      <linearGradient id="g-pink" x1="0" y1="0" x2="0" y2="1"><stop offset="0" stop-color="var(--pink-a)"/><stop offset="1" stop-color="var(--pink-b)"/></linearGradient>
      <linearGradient id="g-teal" x1="0" y1="0" x2="0" y2="1"><stop offset="0" stop-color="var(--teal-a)"/><stop offset="1" stop-color="var(--teal-b)"/></linearGradient>
      <linearGradient id="g-purple" x1="0" y1="0" x2="0" y2="1"><stop offset="0" stop-color="var(--purple-a)"/><stop offset="1" stop-color="var(--purple-b)"/></linearGradient>
      <radialGradient id="g-shadow" cx="0.5" cy="0.5" r="0.5"><stop offset="0" stop-color="#000" stop-opacity="0.16"/><stop offset="1" stop-color="#000" stop-opacity="0"/></radialGradient>
      <g id="band">
        <ellipse cx="330" cy="118" rx="220" ry="12" fill="url(#g-shadow)"/>
        <polygon points="70,32 638,0 629,98 70,104" fill="var(--band)"/>
        <polygon points="96,22 108,6 108,22" fill="var(--fold)"/>
      </g>
    </defs>
  </svg>

  <div class="step" style="top:222px">
    <svg width="720" height="138"><use href="#band"/><polygon points="108,6 192,6 192,102 150,84 108,102" fill="url(#g-blue)"/></svg>
    <div class="step-number">01</div>
    <p class="step-text">Understanding what each party seeks and receives from any partnership</p>
  </div>

  <div class="step" style="top:360px">
    <svg width="720" height="138"><use href="#band"/><polygon points="108,6 192,6 192,102 150,84 108,102" fill="url(#g-yellow)"/></svg>
    <div class="step-number">02</div>
    <p class="step-text">Formal disclosure of personal financial or other relationships for investigators and faculty researchers involved in project</p>
  </div>

  <div class="step" style="top:498px">
    <svg width="720" height="138"><use href="#band"/><polygon points="108,6 192,6 192,102 150,84 108,102" fill="url(#g-green)"/></svg>
    <div class="step-number">03</div>
    <p class="step-text" style="width:430px">Review by organizational and other representatives as needed, to assess and provide recommendations for managing these relationships</p>
  </div>

  <div class="step" style="top:636px">
    <svg width="720" height="138"><use href="#band"/><polygon points="108,6 192,6 192,102 150,84 108,102" fill="url(#g-pink)"/></svg>
    <div class="step-number">04</div>
    <p class="step-text inset" style="top:42px">Recommendation by independent officials on how to address any situation</p>
  </div>

  <div class="step" style="top:774px">
    <svg width="720" height="138"><use href="#band"/><polygon points="108,6 192,6 192,102 150,84 108,102" fill="url(#g-teal)"/></svg>
    <div class="step-number">05</div>
    <p class="step-text inset">Management/Resolution by academic parties in conjunction with their institutions, as well as management plans by industry</p>
  </div>

  <div class="step" style="top:912px">
    <svg width="720" height="138"><use href="#band"/><polygon points="108,6 192,6 192,102 150,84 108,102" fill="url(#g-purple)"/></svg>
    <div class="step-number">06</div>
    <p class="step-text inset" style="top:42px">Appropriate contract mechanisms that reflect proposed workplan and management plan</p>
  </div>
</div>
</body>
</html>
```